R.T.Pell Logging Web design

Our website needs a redesign. We want it to appear professional and easy to navigate. We will be adding videos and pictures to the new website. We do not sell any products on our website. It should be designed for informational purposes. Our company performs timber harvesting and forest management services. Attached is our new company logo.

www.rtpelllogging-example.com if you want to see our current website.

Industry/Entity Type

Graphic Design

Coding

Coded - Design and coding required

```html
<!DOCTYPE html>
<html lang="en">
<head>
<meta charset="utf-8">
<title>R.T. Pell Logging Company</title>
<link href="https://fonts.googleapis.com/css2?family=Lato:wght@400;700&family=PT+Sans:ital,wght@0,400;0,700;1,700&display=swap" rel="stylesheet">
<style>
:root{
  --gold:#e3b04a;
  --gold-soft:#e6b44c;
  --amber:#c98a2e;
  --brown-dark:#5a3212;
  --frame:#3b200f;
  --frame-deep:#1a0d06;
  --rule:#2a1408;
  --bg-top:#c8902e;
  --bg-mid:#7a4e1e;
  --bg-bottom:#33200f;
  --hero-top:#9a7a44;
  --hero-bottom:#3a2a16;
  --video-light:#c0405a;
  --video-dark:#4a0e1c;
}
*{margin:0;padding:0;box-sizing:border-box}
html,body{width:1200px;height:872px;overflow:hidden}
body{
  position:relative;
  background:
    radial-gradient(ellipse 620px 300px at 600px 60px, var(--bg-top) 0%, rgba(200,144,46,.55) 45%, rgba(200,144,46,0) 100%),
    linear-gradient(180deg, #a06a24 0px, var(--bg-mid) 230px, #4a2f15 520px, var(--bg-bottom) 872px);
  font-family:"PT Sans", Arial, sans-serif;
  color:var(--gold-soft);
}
.brand{position:absolute;left:0;top:44px;width:1200px;display:flex;justify-content:center;align-items:center;gap:16px}
.brand-mark{width:60px;height:60px;background:var(--brown-dark);border-radius:8px}
.brand-name{font-family:"PT Sans",Arial,sans-serif;font-weight:700;font-size:38px;line-height:1;color:var(--brown-dark);text-transform:uppercase}
.main-nav{position:absolute;top:143px;left:0;width:1200px;height:34px;font-family:Lato,Arial,sans-serif;font-size:20px;letter-spacing:-0.4px;color:var(--brown-dark)}
.main-nav a{position:absolute;top:0;line-height:34px;text-decoration:none;color:inherit;text-transform:uppercase}
.main-nav .current{left:201px;width:81px;text-align:center;background:var(--amber);border-radius:17px;box-shadow:inset 0 0 0 1px rgba(255,210,120,.5);color:#5e3a16}
.slider{position:absolute;left:192px;top:205px;width:820px;height:296px;background:linear-gradient(180deg,#4a2812,var(--frame) 60%,#2a150a)}
.slide-photo{position:absolute;left:25px;top:13px;width:770px;height:252px;
  background:linear-gradient(180deg,var(--hero-top),var(--hero-bottom))}
.slide-caption{position:absolute;left:11px;top:163px;width:367px;font-family:Lato,Arial,sans-serif;font-weight:700;font-size:14px;line-height:18px;letter-spacing:-0.1px;color:var(--gold);text-align:justify}
.slider-arrow{position:absolute;top:308px;width:44px;height:92px;background:var(--frame)}
.slider-arrow.prev{left:150px;border-radius:46px 0 0 46px}
.slider-arrow.next{left:1011px;border-radius:0 46px 46px 0}
.slider-arrow svg{position:absolute;top:32px}
.slider-arrow.prev svg{left:12px}
.slider-arrow.next svg{left:8px}
.section-title{position:absolute;top:515px;font-family:"PT Sans",Arial,sans-serif;font-weight:700;font-size:24px;line-height:30px;color:var(--gold);text-transform:uppercase}
.welcome-title{left:193px}
.video-title{left:751px}
.welcome-text{position:absolute;left:194px;top:563px;width:530px;font-size:13px;line-height:18px;color:var(--gold-soft)}
.welcome-text p{margin-bottom:18px}
.video-frame{position:absolute;left:749px;top:569px;width:263px;height:188px;background:var(--frame-deep)}
.video-still{position:absolute;left:17px;top:16px;width:229px;height:156px;
  background:linear-gradient(135deg,var(--video-light),var(--video-dark))}
.video-still svg{position:absolute;left:88px;top:46px}
.footer-rule{position:absolute;left:192px;top:781px;width:816px;height:2px;background:var(--rule)}
.copyright{position:absolute;left:192px;top:802px;font-family:Arial,sans-serif;font-style:italic;font-weight:700;font-size:12px;color:#d9a545}
.social-label{position:absolute;left:777px;top:801px;font-family:Arial,sans-serif;font-style:italic;font-weight:700;font-size:14px;color:#d9a545}
.social-link{position:absolute;top:793px;width:35px;height:35px;border-radius:50%;background:var(--amber)}
</style>
</head>
<body>
<header>
  <div class="brand">
    <span class="brand-mark"></span>
    <span class="brand-name">R.T. Pell Logging Company</span>
  </div>
  <nav class="main-nav">
    <a class="current" href="#">Home</a>
    <a href="#" style="left:349px">About Us</a>
    <a href="#" style="left:527px">Services</a>
    <a href="#" style="left:692px">Location</a>
    <a href="#" style="left:866px">Contact Us</a>
  </nav>
</header>

<section class="slider">
  <div class="slide-photo" role="img" aria-label="Photo of a sunset over a grassy field with trees">
    <p class="slide-caption">We are always buying timber in southeast Texas. Call for a free estimate. If you have a timber exemption on your property, call us. We can write timber management plans for you.</p>
  </div>
</section>
<a class="slider-arrow prev" href="#" aria-label="Previous slide"><svg width="22" height="28" viewBox="0 0 22 28"><path d="M17 3 L6 14 L17 25" fill="none" stroke="#c98a2e" stroke-width="5" stroke-linecap="round" stroke-linejoin="round"/></svg></a>
<a class="slider-arrow next" href="#" aria-label="Next slide"><svg width="22" height="28" viewBox="0 0 22 28"><path d="M5 3 L16 14 L5 25" fill="none" stroke="#c98a2e" stroke-width="5" stroke-linecap="round" stroke-linejoin="round"/></svg></a>

<h1 class="section-title welcome-title">Welcome R.T. Pell Logging Company</h1>
<div class="welcome-text">
  <p>Receive high-quality professional logging and land clearing services, from R.T. Pell Logging Company based in Pine Hollow, TX. Whether your tract is large or small, our team of experts can provide the resources and solutions you need to get the job done right. Our track record for consistency, timely service, and expertise will continue to keep us competitive in the East Texas timber industry. We pay top dollar for your pine and hardwood timber.</p>
  <p>To speak with an experienced member of staff, simply contact us 936-555-0142 at your earliest convenience.</p>
  <p>Our office hours are:7am-8pm</p>
</div>

<h2 class="section-title video-title">Video</h2>
<div class="video-frame">
  <div class="video-still" role="img" aria-label="Video preview image">
    <svg width="52" height="52" viewBox="0 0 52 52"><circle cx="26" cy="26" r="26" fill="#c9913f"/><path d="M21 15 L36 26 L21 37 Z" fill="#4a2410"/></svg>
  </div>
</div>

<footer>
  <div class="footer-rule"></div>
  <p class="copyright">© 2010. R.T. Pell Logging Company. ALL RIGHTS RESERVED.</p>
  <span class="social-label">Follow Us :</span>
  <a class="social-link" href="#" style="left:856px" aria-label="Social link 1"></a>
  <a class="social-link" href="#" style="left:896px" aria-label="Social link 2"></a>
  <a class="social-link" href="#" style="left:935px" aria-label="Social link 3"></a>
  <a class="social-link" href="#" style="left:975px" aria-label="Social link 4"></a>
</footer>
</body>
</html>
```